Website Design for Cirruvault As a Service

We are building a service to allow customers to own their own private clouds easily and cheaply. Owning your own private cloud saves costs, and offers more flexibility than a public cloud provider but has historically been a complex and expensive option.

We plan to offer a service where we build and maintain your own private cloud on your own hardware for a cheap monthly costs. Similar to this service - https://stackorra.com/solutions/private-cloud

We already have a logo and branding in place - we'd like a website design to be tailored from this branding, see attached logo design.

Feel free to add important elements on the home page such as testimonials, client/partner logos, contact form, social media, etc using placeholder contents in addition to the document we attached.

We also plan to add sub-pages in the future so please make sure that your website design has a full navigation menu.

An example of the site we like: https://www.verimoxa.com/ we'd be happy for you to take inspiration from this website.

Target Market(s)

B2B focused, we are targeting start-up/small/medium sized companies who needs help with their cloud and IT infrastructure.

Industry/Entity Type

IT

Number of Pages Required

1 page

Font styles to use
Other font styles liked:
• Please refer to the attachment - font must have Mayeka Demi Bold & Retroica

Requirements
Must have
• Please add placeholder menu since we're planning to have subpages later on.

```html
<!DOCTYPE html>
<html lang="en">
<head>
<meta charset="utf-8">
<title>Cirruvault — Private Cloud as a Service</title>
<link href="https://fonts.googleapis.com/css2?family=Lexend:wght@400;500;600&family=Quicksand:wght@400;500;600&display=swap" rel="stylesheet">
<style>
:root{
  --navy:#0b1c26;
  --orange:#f7931e;
  --blue:#2f86dd;
  --ink:#16222b;
  --muted:#3c4852;
  --card:#f3f7fa;
  --line:#2c4c5c;
  --soft:#f7f9fb;
  --white:#ffffff;
}
*{box-sizing:border-box;margin:0;padding:0}
html,body{width:1200px;height:4979px;overflow:hidden}
body{position:relative;background:var(--white);font-family:"Quicksand",sans-serif;color:var(--ink)}
.abs{position:absolute}
h1,h2,h3,h4{font-family:"Lexend",sans-serif;font-weight:500}
.accent-bar{position:absolute;width:80px;height:4px;background:var(--orange)}
.btn{position:absolute;display:flex;align-items:center;justify-content:center;background:var(--orange);color:#fff;font-family:"Quicksand",sans-serif;font-weight:600;font-size:15px;text-decoration:none}
.btn-outline{background:transparent;border:2px solid var(--orange);color:var(--orange);font-size:18px}
.brand{display:flex;align-items:center;gap:10px;font-family:"Lexend",sans-serif;font-weight:600;font-size:26px;color:var(--ink)}
.brand-mark{width:26px;height:26px;border-radius:50%;background:var(--blue)}

/* Header */
.site-nav{position:absolute;left:397px;top:52px;display:flex;gap:34px;font-size:15px;font-weight:500}
.site-nav .active{color:var(--orange)}
.caret::after{content:"▾";font-size:11px;margin-left:4px}

/* Hero */
.hero-title{left:58px;top:196px;width:640px;font-size:42px;line-height:53px;color:var(--ink);white-space:nowrap}
.hero-text{left:58px;top:440px;width:420px;font-size:15.5px;line-height:23px;color:var(--muted)}

/* Benefit cards */
.benefit-card{position:absolute;width:252px;height:312px;background:var(--card);box-shadow:0 6px 18px rgba(20,40,60,.06);padding:30px 24px}
.benefit-card.dark{background:var(--navy)}
.benefit-card.tall{height:318px}
.benefit-icon{width:84px;height:84px;border-radius:50%;background:var(--orange);border:4px solid var(--ink);margin-bottom:28px}
.benefit-card.dark .benefit-icon{background:transparent;border-color:#fff}
.benefit-card h3{font-size:18px;line-height:23px;color:var(--blue);font-weight:400;margin-bottom:18px}
.benefit-card.dark h3{color:#fff}
.benefit-card p{font-size:16px;line-height:23px;color:var(--muted)}
.benefit-card.dark p{color:#dfe7ec}

/* Transformation */
.transform-title{left:567px;top:1775px;width:600px;font-size:35px;line-height:50px;color:#fff}
.transform-text{left:592px;top:1906px;width:540px;font-size:15.5px;line-height:23px;color:#dbe4ea}
.transform-text p{margin-bottom:10px}
.feature-item{position:absolute;display:flex;align-items:center;gap:12px;color:#fff;font-family:"Lexend",sans-serif;font-size:23px}
.tick{width:20px;height:20px;border-radius:50%;background:var(--blue);display:flex;align-items:center;justify-content:center}
.learn-link{position:absolute;left:813px;top:2309px;color:var(--orange);font-weight:600;font-size:17px}

/* Public cloud */
.info-card{position:absolute;background:var(--card);box-shadow:0 6px 18px rgba(20,40,60,.07);padding:28px 32px}
.info-card.dark{background:var(--navy)}
.info-card h3{font-size:19px;line-height:25px;font-weight:400;margin-bottom:16px;padding-left:60px;position:relative}
.info-card h3 .ico{position:absolute;left:0;top:2px;width:44px;height:40px}
.info-card p{font-size:15.5px;line-height:23px;color:var(--muted);margin-bottom:10px}
.info-card.dark p{color:#dfe7ec}

/* Different */
.diff-title{left:58px;top:3472px;width:420px;font-size:35px;line-height:50px;color:#fff}
.step{position:absolute;width:66px;height:66px;border:2px dashed #2d5f82;border-radius:50%;display:flex;align-items:center;justify-content:center;font-family:"Lexend",sans-serif;font-size:32px;color:#2b6c9e}
.step.active{border-color:var(--orange);color:var(--orange)}
.step-text{position:absolute;font-size:15.5px;line-height:23px;color:#d6e0e7;width:360px}
.step-text.left{text-align:right}
.step-text.active{color:#fff;font-weight:600}

/* Newsletter */
.newsletter{left:0;top:4121px;width:1200px;height:436px;background:var(--soft)}
.newsletter-title{left:0;top:4244px;width:1200px;text-align:center;font-size:35px;color:var(--ink)}
.newsletter-sub{left:180px;top:4312px;width:840px;text-align:center;font-size:15.5px;line-height:23px;color:var(--muted)}
.email-field{left:251px;top:4379px;width:548px;height:56px;background:#fff;border:1px solid #e2e8ed;padding-left:20px;display:flex;align-items:center;font-size:15px;color:var(--muted)}

/* Footer */
.site-footer{left:0;top:4557px;width:1200px;height:422px;background:var(--navy)}
.footer-col{position:absolute;top:4662px}
.footer-col h4{font-weight:400;color:#fff;font-size:17px;margin-bottom:22px}
.footer-col li{list-style:none;color:#dfe7ec;font-size:15px;line-height:27px}
.social{position:absolute;top:4847px;width:24px;height:24px;border:2px solid #fff;border-radius:5px}
</style>
</head>
<body>

<header>
  <div class="brand abs" style="left:58px;top:46px;"><span class="brand-mark"></span>Cirruvault</div>
  <nav class="site-nav">
    <span class="active">Home</span>
    <span class="caret">Products</span>
    <span class="caret">Solutions</span>
    <span>Pricing</span>
    <span>About</span>
  </nav>
  <a class="btn" style="left:983px;top:37px;width:159px;height:52px;">Get Started</a>
</header>

<section class="hero">
  <svg class="abs" style="left:0;top:300px" width="1200" height="640" aria-hidden="true">
    <polygon points="460,340 1200,60 1200,625" fill="var(--navy)"/>
  </svg>
  <div class="abs" role="img" aria-label="Isometric illustration of blue server racks linked to a cloud with an upload arrow" style="left:640px;top:97px;width:490px;height:600px;border-radius:40px;background:radial-gradient(ellipse at 55% 45%,#5aa8f0 0%,#2f7fd8 45%,rgba(47,127,216,0) 72%);"></div>
  <div class="accent-bar" style="left:58px;top:184px;"></div>
  <h1 class="abs hero-title">A Groundbreaking Way<br>For Your Small Business To<br>Benefit From The Power<br>Of The Cloud</h1>
  <p class="abs hero-text">Cirruvault as a Service is here to help small businesses utilise the power of the cloud without complicated set-ups or scary price tags<br>Ready to modernise your infrastructure with a fully managed private cloud solution from CVaaS?</p>
  <a class="btn" style="left:58px;top:609px;width:170px;height:57px;">Contact Us</a>
</section>

<section class="benefits">
  <div class="accent-bar" style="left:58px;top:895px;"></div>
  <h2 class="abs" style="left:58px;top:905px;width:520px;font-size:35px;line-height:54px;">How Do We Benefit Your Business</h2>
  <p class="abs" style="left:58px;top:1040px;width:510px;font-size:15.5px;line-height:23px;color:var(--muted);">Cirruvault as a Service is here to help small businesses utilise the power of the cloud without complicated set-ups or scary price tags</p>
  <a class="btn" style="left:58px;top:1136px;width:180px;height:56px;">Learn more</a>

  <div class="benefit-card" style="left:611px;top:905px;"><div class="benefit-icon"></div><h3>Faster Cloud Solutions</h3><p>our private cloud solutions outpace public clouds</p></div>
  <div class="benefit-card" style="left:890px;top:905px;"><div class="benefit-icon"></div><h3>Totally Flexible</h3><p>get the cloud you want and the latest innovations you need</p></div>

  <div class="benefit-card dark tall" style="left:58px;top:1250px;"><div class="benefit-icon"></div><h3>Greater Value For Money</h3><p>totally transparent pricing for no nasty month-end surprises</p></div>
  <div class="benefit-card tall" style="left:335px;top:1250px;"><div class="benefit-icon"></div><h3>No Consultancy Fees</h3><p>we'll work with you and charge set fees for everything</p></div>
  <div class="benefit-card tall" style="left:611px;top:1250px;"><div class="benefit-icon"></div><h3>Management, Monitoring And Maintenace</h3><p>they're all included in your monthly price</p></div>
  <div class="benefit-card tall" style="left:890px;top:1250px;"><div class="benefit-icon"></div><h3>Tried And Tested Cloud Solutions</h3><p>we'll deploy the right OpenRack solutions for your business</p></div>
</section>

<section class="transform">
  <svg class="abs" style="left:0;top:1687px" width="1200" height="955" aria-hidden="true">
    <defs>
      <linearGradient id="darkSweep" x1="0" y1="0" x2="1" y2="1">
        <stop offset="0" stop-color="#0a1a23"/><stop offset=".45" stop-color="#14323f"/><stop offset="1" stop-color="#0a1a23"/>
      </linearGradient>
    </defs>
    <polygon points="0,0 1200,0 1200,713 0,954" fill="url(#darkSweep)"/>
  </svg>
  <div class="abs" role="img" aria-label="Isometric illustration of server stacks connected by a cable to a cloud" style="left:0;top:1896px;width:540px;height:426px;background:radial-gradient(ellipse at 40% 45%,#4fa0ec 0%,#2b74c6 40%,rgba(43,116,198,0) 70%);"></div>
  <div class="accent-bar" style="left:567px;top:1767px;"></div>
  <h2 class="abs transform-title">CVAAS Can Drive Your Digital Transformation Today</h2>
  <div class="abs transform-text">
    <p>Organisations of all shapes and sizes are reaping the time and money saving benefits that the cloud brings</p>
    <p>But for small businesses seeking to transition, managing the time and financial costs of transitioning, and knowing whether to opt for a public or private cloud can cause you to hit the pause button</p>
    <p>CVAAS is here to help you switch on your cloud transformation in a way that works best for you. We deliver and support fully managed private cloud solutions that are:</p>
  </div>
  <div class="feature-item" style="left:592px;top:2168px;"><span class="tick"><svg width="12" height="12"><path d="M2 6l3 3 5-6" stroke="#fff" stroke-width="2" fill="none"/></svg></span>Fast</div>
  <div class="feature-item" style="left:836px;top:2168px;"><span class="tick"><svg width="12" height="12"><path d="M2 6l3 3 5-6" stroke="#fff" stroke-width="2" fill="none"/></svg></span>Powerful</div>
  <div class="feature-item" style="left:592px;top:2220px;"><span class="tick"><svg width="12" height="12"><path d="M2 6l3 3 5-6" stroke="#fff" stroke-width="2" fill="none"/></svg></span>Easy</div>
  <div class="feature-item" style="left:836px;top:2220px;"><span class="tick"><svg width="12" height="12"><path d="M2 6l3 3 5-6" stroke="#fff" stroke-width="2" fill="none"/></svg></span>Scalable</div>
  <a class="btn" style="left:592px;top:2295px;width:168px;height:52px;">Get Started</a>
  <a class="learn-link">Learn more <svg width="20" height="14" style="vertical-align:middle;margin-left:6px"><path d="M1 7h16M11 2l6 5-6 5" stroke="var(--orange)" stroke-width="2" fill="none"/></svg></a>
</section>

<section class="public-cloud">
  <div class="accent-bar" style="left:58px;top:2707px;"></div>
  <h2 class="abs" style="left:58px;top:2728px;width:480px;font-size:35px;line-height:54px;">If You're Using A Public Cloud Now</h2>
  <div class="info-card" style="left:58px;top:2873px;width:519px;height:204px;">
    <h3 style="color:#e53935;"><svg class="ico" viewBox="0 0 44 40"><circle cx="20" cy="20" r="15" stroke="#e53935" stroke-width="3" fill="none"/><circle cx="20" cy="20" r="6" fill="#e53935"/></svg>You're Likely Not Getting The Benefits Of Full Functionality</h3>
    <p>Public cloud providers cannot adopt new innovations and functions as quickly and easily as the private cloud solutions you'll get from CVAAS</p>
  </div>
  <div class="info-card" style="left:619px;top:2724px;width:523px;height:208px;">
    <h3 style="color:#3aa335;"><svg class="ico" viewBox="0 0 44 40"><circle cx="22" cy="12" r="10" fill="#3aa335"/><path d="M2 30c10-4 20 6 40-4" stroke="#3aa335" stroke-width="4" fill="none"/></svg>You Could Be Paying Too Much</h3>
    <p>Public cloud pricing structures have a habit of sneakily scaling up very quickly</p>
    <p>With CVAAS, you'll always know what you're paying for your private cloud services</p>
  </div>
  <div class="info-card dark" style="left:619px;top:2966px;width:523px;height:207px;">
    <h3 style="color:#fff;"><svg class="ico" viewBox="0 0 44 40"><circle cx="15" cy="20" r="9" stroke="#7f6ff0" stroke-width="4" fill="none"/><circle cx="29" cy="20" r="9" stroke="#7f6ff0" stroke-width="4" fill="none"/></svg>You'll Be Tied To The Services Your Provider Can Provide</h3>
    <p>Public cloud providers will have a limited suite of products and services to offer you</p>
    <p>A CVAAS private cloud has no such limitations</p>
  </div>
  <a class="btn btn-outline" style="left:503px;top:3216px;width:194px;height:58px;">Get Started</a>
</section>

<section class="different">
  <svg class="abs" style="left:0;top:3270px" width="1200" height="852" aria-hidden="true">
    <defs>
      <linearGradient id="blueStreak" x1="0" y1="0" x2="1" y2="0">
        <stop offset="0" stop-color="#3b6fe8"/><stop offset="1" stop-color="#9fd0f5" stop-opacity="0"/>
      </linearGradient>
    </defs>
    <polygon points="0,10 760,125 0,155" fill="url(#blueStreak)"/>
    <polygon points="0,155 1200,60 1200,852 0,852" fill="var(--navy)"/>
  </svg>
  <h2 class="abs diff-title">What Makes CVAAS Different</h2>
  <a class="btn" style="left:952px;top:3508px;width:190px;height:52px;">Pick Your Plan</a>

  <svg class="abs" style="left:0;top:3600px" width="1200" height="440" aria-hidden="true">
    <line x1="551" y1="84" x2="551" y2="133" stroke="var(--orange)" stroke-width="2" stroke-dasharray="4 4"/>
    <line x1="551" y1="200" x2="551" y2="250" stroke="#2d5f82" stroke-width="2" stroke-dasharray="4 4"/>
    <line x1="551" y1="317" x2="551" y2="366" stroke="#2d5f82" stroke-width="2" stroke-dasharray="4 4"/>
    <line x1="648" y1="84" x2="648" y2="133" stroke="#2d5f82" stroke-width="2" stroke-dasharray="4 4"/>
    <line x1="648" y1="200" x2="648" y2="250" stroke="#2d5f82" stroke-width="2" stroke-dasharray="4 4"/>
    <line x1="648" y1="317" x2="648" y2="366" stroke="#2d5f82" stroke-width="2" stroke-dasharray="4 4"/>
  </svg>

  <div class="step" style="left:518px;top:3618px;">1</div>
  <div class="step active" style="left:518px;top:3734px;">2</div>
  <div class="step" style="left:518px;top:3851px;">3</div>
  <div class="step" style="left:518px;top:3967px;">4</div>
  <div class="step" style="left:615px;top:3618px;">5</div>
  <div class="step" style="left:615px;top:3734px;">6</div>
  <div class="step" style="left:615px;top:3851px;">7</div>
  <div class="step" style="left:615px;top:3967px;">8</div>

  <p class="step-text left" style="left:128px;top:3617px;">We'll quickly get to grips with what your organisation needs, and deliver it via our private cloud solutions</p>
  <p class="step-text left active" style="left:128px;top:3745px;">Managed operations from private OpenRack clouds and Helmsway</p>
  <p class="step-text left" style="left:128px;top:3850px;">You can focus on your core business while we support you with a dedicated cloud infrastructure</p>
  <p class="step-text left" style="left:128px;top:3978px;">Fast and easy computing, storage and network resources</p>
  <p class="step-text" style="left:712px;top:3628px;">We'll create and deliver the launchpad that will take your business forward</p>
  <p class="step-text" style="left:712px;top:3733px;">Get the benefits of your own cloud infrastructure and reduce your operational costs</p>
  <p class="step-text" style="left:712px;top:3850px;width:380px;">Enjoy the ease of the public cloud, combined with the features, innovations and flexibility of the private cloud</p>
  <p class="step-text" style="left:712px;top:3978px;">We'll support your growth and scale your cloud as you need it</p>
</section>

<section class="newsletter-block">
  <div class="abs newsletter"></div>
  <div class="accent-bar" style="left:560px;top:4213px;"></div>
  <h2 class="abs newsletter-title">Join Our Newsletter</h2>
  <p class="abs newsletter-sub">Join Now And Recieve E-Mail Updates On New Solutions And Services, Special Promotions, New Deals And More</p>
  <div class="abs email-field">Enter Your Email</div>
  <a class="btn" style="left:799px;top:4379px;width:151px;height:56px;">Join Now</a>
</section>

<footer>
  <div class="abs site-footer"></div>
  <div class="brand abs" style="left:58px;top:4645px;color:#fff;font-size:24px;"><span class="brand-mark"></span>Cirruvault</div>
  <p class="abs" style="left:58px;top:4702px;width:260px;font-size:15px;line-height:24.5px;color:#dfe7ec;">Cirruvault as a Service is here to help small businesses utilise the power of the cloud without complicated set-ups or scary price tags</p>
  <span class="social" style="left:58px;"></span>
  <span class="social" style="left:104px;"></span>
  <span class="social" style="left:152px;"></span>

  <div class="footer-col" style="left:406px;"><h4>Navgation</h4><ul><li>Home</li><li>Products</li><li>Solutions</li><li>Pricing</li><li>About Us</li></ul></div>
  <div class="footer-col" style="left:557px;"><h4>Support</h4><ul><li>FAQs</li><li>Customer Support</li><li>Help</li><li>Request a Demo</li></ul></div>
  <div class="footer-col" style="left:751px;"><h4>Company</h4><ul><li>Leadership</li><li>Newsroom</li><li>Customers</li><li>Partners</li><li>Careers</li></ul></div>
  <div class="footer-col" style="left:904px;"><h4>Contact Us</h4><ul>
    <li>☎&nbsp; +1 345 555 0182</li>
    <li>☎&nbsp; +1 345 555 0195</li>
    <li>✉&nbsp; contact@cirruvault.com</li></ul></div>

  <div class="abs" style="left:58px;top:4900px;width:1084px;height:1px;background:var(--line);"></div>
  <p class="abs" style="left:58px;top:4930px;font-size:15px;color:#dfe7ec;">© 2022 Cirruvault Services</p>
  <p class="abs" style="left:862px;top:4930px;font-size:15px;color:#dfe7ec;">Privacy Policy &nbsp;&nbsp;|&nbsp;&nbsp; Terms Of Service</p>
</footer>

</body>
</html>
```